Business card for utility of the future

I need a business card template designed for brivolo. We provide sustainable water, energy and waste services to homes.

The card should include name, position, email address, phone number, website and our logo (attached). I would like it to convey professionalism and creativity.

Target Market(s)

Homeowners, investors, corporate partners.

Industry/Entity Type

Utility

Contact Information for Business Card

The card should include name, position, email address, phone number, website and our logo (attached).

```html
<!DOCTYPE html>
<html lang="en">
<head>
<meta charset="utf-8">
<title>brivolo business card</title>
<link href="https://fonts.googleapis.com/css2?family=Open+Sans:wght@400;600;700&display=swap" rel="stylesheet">
<style>
  :root {
    --coral: #ef8466;
    --leaf: #6abf82;
    --ink: #3a3a3a;
    --paper: #ffffff;
    --backdrop: #ecebe8;
  }
  * { box-sizing: border-box; margin: 0; padding: 0; }
  html, body {
    width: 1200px; height: 900px; overflow: hidden;
    background: var(--backdrop);
    font-family: "Open Sans", Arial, sans-serif;
  }
  .canvas {
    position: relative; width: 1200px; height: 900px;
    display: flex; flex-direction: column; align-items: center;
    justify-content: center; gap: 30px;
  }
  .card {
    position: relative; width: 700px; height: 400px; overflow: hidden;
    box-shadow: 0 6px 18px rgba(0,0,0,0.12);
  }

  /* Shared company name */
  .company-name {
    position: absolute;
    font-weight: 600; line-height: 1; white-space: nowrap;
  }

  /* Back side */
  .card--back { background: var(--coral); }
  .card--back .company-name {
    left: 50%; top: 50%; transform: translate(-50%, -50%);
    font-size: 110px; color: var(--paper);
  }

  /* Front side */
  .card--front { background: var(--paper); }
  .corner-mark { position: absolute; left: 0; top: 0; }
  .person { position: absolute; left: 74px; top: 22px; }
  .person__name { color: var(--leaf); font-weight: 700; font-size: 19px; line-height: 1.3; }
  .person__role { color: var(--ink); font-size: 14px; line-height: 1.3; }

  .card--front .company-name {
    right: 60px; top: 140px;
    font-size: 96px; color: var(--ink);
  }

  .contact {
    position: absolute; left: 36px; top: 226px; list-style: none;
    color: var(--ink); font-size: 16px;
  }
  .contact li { display: flex; align-items: center; gap: 12px; height: 25px; }
  .contact svg { width: 13px; height: 13px; fill: var(--leaf); flex: none; }

  .bands { position: absolute; left: 0; top: 0; }
</style>
</head>
<body>
<main class="canvas">

  <section class="card card--back" aria-label="Card back">
    <p class="company-name">brivolo</p>
  </section>

  <section class="card card--front" aria-label="Card front">
    <svg class="corner-mark" width="70" height="60" viewBox="0 0 70 60">
      <polygon points="0,22 26,22 14,40 0,40" fill="var(--coral)"/>
      <polygon points="34,22 62,22 50,50 18,50" fill="var(--leaf)"/>
    </svg>

    <div class="person">
      <p class="person__name">Marcus Hale</p>
      <p class="person__role">Managing Director</p>
    </div>

    <p class="company-name">brivolo</p>

    <ul class="contact">
      <li>
        <svg viewBox="0 0 16 16"><path d="M3.6 1.2l2.3 2.6-1.3 1.9c.9 2 2.6 3.8 4.7 4.7l1.9-1.3 2.6 2.3-1.6 2.6C6.5 13.8 2.2 9.5 1 3.1z"/></svg>
        044-987 650 321
      </li>
      <li>
        <svg viewBox="0 0 16 16"><path d="M1 3h14v10H1z M1.5 3.5L8 9l6.5-5.5" stroke="#fff" stroke-width="1.2"/></svg>
        hello@brivolo.com
      </li>
      <li>
        <svg viewBox="0 0 16 16"><circle cx="8" cy="8" r="7"/><path d="M1 8h14M8 1c-3 3.5-3 10.5 0 14M8 1c3 3.5 3 10.5 0 14" stroke="#fff" stroke-width="1" fill="none"/></svg>
        www.brivolo.com
      </li>
    </ul>

    <svg class="bands" width="700" height="400" viewBox="0 0 700 400">
      <polygon points="0,334 296,334 276,370 0,370" fill="var(--coral)"/>
      <polygon points="292,346 700,346 700,400 262,400" fill="var(--leaf)"/>
    </svg>
  </section>

</main>
</body>
</html>
```